Heath Weight Loss Retreat Website

The brief:
PineLoop is a provider of health & weight loss retreats and wish to redesign their main website. The website needs to provide detailed information about the company’s services whilst gathering the maximum number of leads possible. The website does not aim to get clients to ‘book now’ but to request further information, or ask a question generating a lead/opportunity for the business.

Primary objectives of website
• Gather leads for products (not necessarily to book at that point, but to ‘request more info’)
• Provide detailed information about the health and fitness programs on offer

Demographic Considerations
• Target age group: 30-50
• Predominant client base are female but website should be gender neutral due to some men attending

Design considerations
• Essentially selling ‘travel experiences’ and ‘life transformations’ so needs to be lots of images to display (similar to a hotel website for example)
• Images need to display real people – i.e. larger people, rather than super thin
• Not too much use of flash
• SEO friendly (we have good rankings at present)
• Will be implemented into Joomla, so please consider this on the design
• Colours should be ‘warm’ and ‘friendly’ and gender neutral

Project Requirements & Expectations
Please supply your design ideas with:
• At least 1 (preferably more) homepage examples
• At least 1 (preferably more) internal page examples
Once a preferred design has been selected the following will be produced, tweaked and approved:
• Homepage + 1 internal landing page + 1 internal main page + 1 contact page + 1 info request page

Attachments
We have attached both a homepage and internal page example which demonstates the type of content needed and the calls to action. This is for demonstration purposes only so please ignore colours, fonts, etc and provide your best designs based on a general layout as per attached.

Images:
A selection of example images has been attached. For the homepage images of the retreats themselves should be used alongside images of ‘larger people’.

Further information:
Please contact Simon Thackery at simon.thackery@coralbeaconfiles.com.au

Target Market(s)

Overweight females aged 30-50 are the main target market. However must be gender neutral due to some men using product.

Industry/Entity Type

Weight

Requirements
Should not have
• Not too much flash

```html
<!DOCTYPE html>
<html lang="en">
<head>
<meta charset="utf-8">
<title>PineLoop – Weight Loss Retreat</title>
<link href="https://fonts.googleapis.com/css2?family=Arimo:ital,wght@0,400;0,700;1,700&display=swap" rel="stylesheet">
<style>
:root{
  --green:#7ab526;
  --green-dark:#4f8a12;
  --green-deep:#3d6e0c;
  --green-pale:#eef6dc;
  --orange:#f28a1a;
  --orange-dark:#d96d06;
  --text:#555;
  --line:#dcdcdc;
  --white:#fff;
}
*{box-sizing:border-box;margin:0;padding:0}
html,body{width:876px;height:1200px;overflow:hidden;background:var(--white)}
body{font-family:"Arimo",Arial,sans-serif;color:var(--text);font-size:11px;position:relative}
.abs{position:absolute}
ul{list-style:none}

/* header */
.header{top:0;left:0;width:876px;height:170px;background:linear-gradient(#fff,#f5f9ec)}
.brand-name{left:22px;top:38px;font-size:32px;font-weight:700;color:var(--green-dark)}
.brand-tag{left:24px;top:80px;font-size:9px;color:var(--green-dark);letter-spacing:1px}
.head-col{top:30px;width:140px}
.head-col h4{color:var(--green);font-size:11px;margin-bottom:5px}
.head-col li{font-size:9.5px;line-height:14px;padding-left:10px;position:relative}
.head-col li:before{content:"";position:absolute;left:0;top:5px;width:4px;height:4px;background:var(--green)}
.mag{left:760px;top:18px;width:100px;height:140px;background:linear-gradient(#ffe9d0,#f3b06a);border:1px solid var(--line)}
.mag-free{left:8px;top:8px;font-size:22px;font-weight:700;font-style:italic;color:var(--white)}
.mag-label{left:8px;top:40px;font-size:9.5px;color:var(--green-deep);font-weight:700}

/* nav */
.nav{top:170px;left:0;width:876px;height:28px;background:linear-gradient(var(--green),var(--green-dark));display:flex;justify-content:space-around;align-items:center}
.nav a{color:var(--white);font-size:11px;font-weight:700;text-decoration:none}

/* hero */
.hero{top:198px;left:0;width:876px;height:240px;background:linear-gradient(var(--green-pale),#dcedb6)}
.hero-photo{left:20px;top:0;width:200px;height:240px;background:linear-gradient(#d7e6c0,#9db97a)}
.hero-title{left:230px;top:40px;width:646px;height:40px;background:linear-gradient(90deg,var(--orange),#f7ad55);color:var(--white);font-size:26px;font-weight:700;padding:5px 20px}
.hero-lead{left:250px;top:100px;width:520px;font-size:17px;line-height:22px;font-weight:700;color:var(--green-dark)}
.btn{height:36px;border-radius:18px;background:linear-gradient(#f9a43f,var(--orange-dark));color:var(--white);font-size:16px;font-weight:700;display:flex;align-items:center;justify-content:center;gap:8px;border:2px solid #fff}
.btn-book{left:400px;top:170px;width:165px}
.btn-info{left:575px;top:170px;width:265px}
.arrow{width:16px;height:16px;border-radius:50%;background:var(--white);color:var(--orange);font-size:10px;display:flex;align-items:center;justify-content:center}

/* sidebar */
.side{top:438px;left:0;width:210px}
.side-head{height:32px;background:var(--orange);color:var(--white);font-size:15px;font-weight:700;padding:8px 18px}
.side-menu{background:linear-gradient(var(--green),var(--green-dark));padding:6px 0}
.side-menu li{color:var(--white);font-size:10.5px;font-weight:700;height:23px;line-height:23px;padding-left:34px;position:relative;border-bottom:1px solid rgba(255,255,255,.2)}
.side-menu li:before{content:"›";position:absolute;left:20px;color:#fff}
.side-tabs{padding:8px 0}
.side-tabs li{height:24px;line-height:24px;padding-left:18px;font-size:14px;font-weight:700;color:var(--orange);margin-bottom:4px;background:linear-gradient(90deg,#fff 70%,#fde5c8)}
.quick{background:var(--green-pale);padding:8px 16px 12px}
.quick h3{background:var(--green);color:var(--white);font-size:13px;margin:-8px -16px 8px;padding:6px 16px}
.quick label{display:block;font-size:10px;margin:4px 0 2px}
.field{height:18px;background:var(--white);border:1px solid var(--line)}
.field.tall{height:46px}
.submit{margin:8px 0 0 auto;width:60px;height:18px;background:var(--green-dark);color:var(--white);font-size:9px;text-align:center;line-height:18px}

/* tiles */
.tiles{top:450px;left:222px;width:648px;display:flex;gap:6px}
.tile{flex:1;height:140px;background:linear-gradient(var(--green),var(--green-dark));color:var(--white);font-size:18px;font-weight:700;font-style:italic;line-height:21px;text-align:center;padding-top:14px;border-bottom:4px solid var(--orange)}
.tile-icon{width:80px;height:54px;margin:12px auto 0;border-radius:4px;background:linear-gradient(#fff,#f2e4cc)}
.tile-icon.map{background:linear-gradient(#cfe8a0,#8fc54a)}
.tile-icon.cal{background:linear-gradient(#fff,#dfe6ee)}
.tile-icon.people{background:linear-gradient(#f3dcc4,#d9a77a)}

/* content */
.h2{font-size:18px;color:#444;font-weight:400}
.change-1{left:240px;top:606px}
.photo{height:130px;background:linear-gradient(#e7d9c8,#b99d84)}
.photo-a{left:240px;top:636px;width:150px}
.photo-b{left:400px;top:636px;width:150px;background:linear-gradient(#dfe8cf,#a6b98c)}
.intro{left:570px;top:638px;width:290px}
.intro strong{display:block;color:var(--orange);font-size:11.5px;line-height:15px;margin-bottom:8px}
.intro p{font-size:10px;line-height:14px}
.change-2{left:240px;top:782px}
.steps{left:240px;top:814px;width:620px;display:grid;grid-template-columns:1fr 1fr;column-gap:30px;row-gap:14px}
.step h5{font-size:11px;color:var(--orange);border-bottom:1px solid var(--line);padding-bottom:4px;margin-bottom:5px}
.step h5 span{color:var(--green-dark)}
.step p{font-size:10px;line-height:14px}

/* footer */
.footer{top:1036px;left:0;width:876px;height:134px;background:var(--green-pale);border-top:4px solid var(--green);display:flex;padding:14px 20px;gap:22px}
.footer .col{flex:1}
.footer h4{color:var(--green-dark);font-size:10.5px;margin-bottom:6px}
.footer li{font-size:9.5px;line-height:14px;padding-left:9px;position:relative}
.footer li:before{content:"";position:absolute;left:0;top:5px;width:4px;height:4px;background:var(--orange)}
.bottom{top:1170px;left:0;width:876px;height:30px;background:var(--green-dark);color:var(--white);font-size:10px;display:flex;justify-content:space-between;align-items:center;padding:0 20px}
</style>
</head>
<body>

<header class="header abs">
  <div class="brand-name abs">PineLoop</div>
  <div class="brand-tag abs">WEIGHT LOSS RETREAT</div>

  <div class="head-col abs" style="left:250px">
    <h4>The Best Programs</h4>
    <ul><li>Weight Loss Retreat</li><li>Residential Boot Camp</li><li>Fitness Days</li><li>At home program</li><li>Local group exercise</li></ul>
  </div>
  <div class="head-col abs" style="left:400px">
    <h4>The Best Locations</h4>
    <ul><li>Blue Mountains, NSW</li><li>Sunshine Coast, QLD</li><li>Local Programs</li></ul>
  </div>
  <div class="head-col abs" style="left:550px;width:160px">
    <h4>And now and get Results</h4>
    <ul><li>Why choose PineLoop</li><li>Expert Team</li><li>What clients say</li><li>Contact us</li><li>FREE Brochure</li></ul>
  </div>

  <div class="mag abs" role="img" aria-label="Cover of the free PineLoop magazine">
    <div class="mag-free abs">free</div>
    <div class="mag-label abs">PineLoop Magazine</div>
  </div>
</header>

<nav class="nav abs">
  <a>ABOUT US</a><a>NUTRITION</a><a>OUR DIETS</a><a>HEALTH</a><a>EXERCISE</a><a>CONTACT US</a>
</nav>

<section class="hero abs">
  <div class="hero-photo abs" role="img" aria-label="Photo of a smiling retreat guest"></div>
  <h1 class="hero-title abs">Weight Loss Retreat</h1>
  <p class="hero-lead abs">Lasting weight loss and lifestyle change for people<br>of all ages, shapes, sizes and fitness levels.</p>
  <div class="btn btn-book abs">Book Now <span class="arrow">▶</span></div>
  <div class="btn btn-info abs">Request more information <span class="arrow">▶</span></div>
</section>

<aside class="side abs">
  <div class="side-head">Weight Loss Retreat</div>
  <ul class="side-menu">
    <li>Overview</li><li>Program Details</li><li>Available locations</li><li>Is it suitable for you?</li><li>Typical Day</li><li>Book Food</li><li>Valuable education</li><li>Lasting results</li><li>Photo Gallery</li><li>Testimonials</li>
  </ul>
  <ul class="side-tabs">
    <li>Dates &amp; Rates</li><li>Book Now</li><li>Contact Us</li>
  </ul>
  <div class="quick">
    <h3>Quick Contact</h3>
    <label>E-mail</label><div class="field"></div>
    <label>Question</label><div class="field tall"></div>
    <div class="submit">SUBMIT</div>
  </div>
</aside>

<div class="tiles abs">
  <div class="tile">Download<br>Brochure<div class="tile-icon" role="img" aria-label="Brochure cover picture"></div></div>
  <div class="tile">Available<br>locations<div class="tile-icon map" role="img" aria-label="Map of retreat locations"></div></div>
  <div class="tile">Dates<br>and Costs<div class="tile-icon cal" role="img" aria-label="Calendar picture"></div></div>
  <div class="tile">What Clients<br>Say...<div class="tile-icon people" role="img" aria-label="Photo of happy clients"></div></div>
</div>

<h2 class="h2 change-1 abs">Change your life with us</h2>
<div class="photo photo-a abs" role="img" aria-label="Photo of guests exercising at the retreat"></div>
<div class="photo photo-b abs" role="img" aria-label="Photo of a guest after her transformation"></div>
<div class="intro abs">
  <strong>Hundreds of people have already transformed their lives with PineLoop's proven program</strong>
  <p>PineLoop you will lose weight, lose centimetres, get fit and experience lasting health and fitness results in a friendly, supportive retreat setting.</p>
</div>

<h2 class="h2 change-2 abs">Change your life with us</h2>
<div class="steps abs">
  <div class="step"><h5><span>01.</span> COUNT CALORIES</h5><p>Our Weight Loss Retreat program is suitable for people of all ages, shapes, sizes and fitness levels.</p></div>
  <div class="step"><h5><span>01.</span> COUNT CALORIES</h5><p>It is amazingly fun and extremely effective with amazing weight loss and fitness results.</p></div>
  <div class="step"><h5><span>01.</span> COUNT CALORIES</h5><p>Whether you want a kick start or are embarking on a long term weight loss program.</p></div>
  <div class="step"><h5><span>01.</span> COUNT CALORIES</h5><p>Our Weight Loss Retreat program will be one of the best experiences of your life.</p></div>
</div>

<footer class="footer abs">
  <div class="col"><h4>The Best Programs</h4><ul><li>Weight Loss Retreat</li><li>Residential Boot Camp</li><li>Fitness Days</li><li>At home program</li><li>Local group exercise</li></ul></div>
  <div class="col"><h4>The Best Locations</h4><ul><li>Blue Mountains, NSW</li><li>Sunshine Coast, QLD</li><li>Local Programs</li></ul></div>
  <div class="col"><h4>About Us</h4><ul><li>Why choose PineLoop</li><li>Expert Team</li><li>What clients say</li><li>Contact us</li><li>FREE Brochure</li></ul></div>
  <div class="col"><h4>Results For...</h4><ul><li>Weight Loss</li><li>Fitness goals</li><li>Diabetes reduction</li><li>Blood pressure reduction</li><li>Depression treatment</li><li>...more health benefits</li></ul></div>
  <div class="col"><h4>Free Information</h4><ul><li>Request a brochure</li><li>FREE PineLoop Magazine</li></ul></div>
</footer>

<div class="bottom abs">
  <span>Contact Us | Book Here | Privacy</span>
  <span>© PineLoop Wellbeing Pty Ltd ABN 48 902 117 365</span>
</div>

</body>
</html>
```